Redesign of page from emergency manual

Please redesign this PDF to look better. Please don't include any stock photos. It must be legible. Making some words bold is probably a good idea.

Here are some things I like :

https://tarrowbooks.com.au/collections/frontpage/products/the-plk-v2-ebook

https://img-cd.vostramediafiles.com/qa-ejkwPLOTYY_SuCKbZNu411Qwgjv8YssPxEdzXN93hDkSRjLXK8WmfgbmrJW4ZZ3yUPK=w1052-h592-rw

```html
<!DOCTYPE html>
<html lang="en">
<head>
<meta charset="utf-8">
<title>Hypertension, Acute</title>
<link rel="stylesheet" href="https://fonts.googleapis.com/css2?family=Montserrat:wght@600;700;800&family=Quicksand:wght@400;500;700&display=swap">
<style>
  :root {
    --blue: #2874b4;
    --teal: #3db5a6;
    --red: #dc4a53;
    --pink: #e2467d;
    --ink: #1b1b22;
    --line: #2a74b5;
    --white: #ffffff;
  }
  * { box-sizing: border-box; margin: 0; padding: 0; }
  html, body { width: 1200px; height: 927px; overflow: hidden; background: var(--white); }
  body { position: relative; font-family: "Quicksand", sans-serif; color: var(--ink); }

  .page-header {
    position: absolute; left: 0; top: 0; width: 1200px; height: 102px;
    background: linear-gradient(90deg, var(--blue), var(--teal));
  }
  .page-title {
    position: absolute; left: 62px; top: 24px; width: 580px; white-space: nowrap;
    font-family: "Montserrat", sans-serif; font-weight: 700; font-size: 44px;
    letter-spacing: -1.5px; line-height: 52px; color: var(--white);
    text-shadow: 2px 2px 0 #145a52;
  }
  .page-subtitle {
    position: absolute; left: 686px; top: 22px; width: 448px;
    text-align: center; font-family: "Montserrat", sans-serif; font-weight: 700;
    font-size: 20px; line-height: 27px; color: var(--white);
    text-shadow: 1px 1px 0 #1d5f70;
  }

  .intro { position: absolute; left: 65px; top: 116px; width: 620px; }
  .intro-lead { font-family: "Montserrat", sans-serif; font-weight: 600; font-size: 18px; line-height: 24px; }
  .intro-list { list-style: none; margin-top: 13px; padding-left: 26px; }
  .intro-list li { position: relative; font-size: 20.5px; line-height: 26px; margin-bottom: 4px; }
  .intro-list li::before {
    content: ""; position: absolute; left: -17px; top: 10px; width: 8px; height: 8px;
    border-radius: 50%; background: #8a8fc4;
  }

  .bp-range {
    position: absolute; left: 710px; top: 122px; width: 422px;
    border-collapse: collapse; border: 2px solid var(--teal); text-align: center;
  }
  .bp-range caption {
    caption-side: top; background: var(--teal); color: var(--white);
    font-family: "Montserrat", sans-serif; font-weight: 700; font-size: 18px; height: 37px; line-height: 37px;
  }
  .bp-range th, .bp-range td { border: 1.5px solid var(--teal); height: 32px; }
  .bp-range th { color: var(--teal); font-family: "Montserrat", sans-serif; font-weight: 700; font-size: 17px; }
  .bp-range td { font-weight: 700; font-size: 18px; }

  .caution {
    position: absolute; left: 67px; top: 304px; width: 1066px; height: 91px;
    background: var(--red); border-radius: 16px; color: var(--white);
  }
  .caution-icon { position: absolute; left: 18px; top: 21px; }
  .caution-text {
    position: absolute; left: 80px; top: 4px; width: 970px;
    font-size: 20px; line-height: 23.5px; text-align: justify; text-align-last: center;
  }
  .caution-label { font-family: "Montserrat", sans-serif; font-weight: 800; font-size: 27px; margin-right: 20px; }

  .drug-table {
    position: absolute; left: 73px; top: 407px; width: 1058px;
    border-collapse: collapse; border: 1.5px solid var(--line);
  }
  .drug-table thead th {
    background: var(--blue); color: var(--white); height: 47px;
    font-family: "Montserrat", sans-serif; font-weight: 700; font-size: 18px;
  }
  .drug-table td { border: 1.5px solid var(--line); vertical-align: middle; font-weight: 700; font-size: 20px; line-height: 24px; }
  .drug-action { width: 239px; padding-left: 12px; }
  .drug-list { list-style: none; padding-left: 28px; }
  .drug-list li { position: relative; }
  .drug-list li::before {
    content: ""; position: absolute; left: -15px; top: 9px; width: 8px; height: 8px;
    border-radius: 50%; background: var(--blue);
  }
  .drug-list .spaced { margin-top: 12px; }

  .differential-title {
    position: absolute; left: 0; top: 773px; width: 1200px; text-align: center;
    font-family: "Montserrat", sans-serif; font-weight: 700; font-size: 26px; color: var(--pink);
  }
  .differential-list { position: absolute; list-style: none; font-weight: 700; font-size: 17px; line-height: 20px; }
  .differential-list li { position: relative; padding-left: 18px; margin-bottom: 8px; }
  .differential-list li::before {
    content: ""; position: absolute; left: 0; top: 6px; width: 8px; height: 8px;
    border-radius: 50%; background: var(--pink);
  }
  .col-a { left: 88px; top: 811px; width: 310px; text-align: justify; letter-spacing: -0.3px; }
  .col-b { left: 473px; top: 811px; width: 260px; }
  .col-c { left: 820px; top: 811px; width: 240px; }
  .col-c li { margin-bottom: 10px; }

  .page-footer {
    position: absolute; left: 0; top: 912px; width: 1200px; height: 15px;
    background: linear-gradient(90deg, var(--blue), var(--teal));
  }
</style>
</head>
<body>
  <header class="page-header">
    <h1 class="page-title">HYPERTENSION, ACUTE</h1>
    <p class="page-subtitle">Sustained high blood pressure refractory<br>to treating reversible causes</p>
  </header>

  <section class="intro">
    <p class="intro-lead">In pediatrics, hypertension is almost always treated by addressing likely causes such as light anesthesia or measurement error:</p>
    <ul class="intro-list">
      <li>Ensure correct BP cuff size: cuff bladder<br>width ~ 40% of limb circumference</li>
      <li>Ensure arterial line transducer is at level of heart<br>Consider placing arterial line if not already present</li>
    </ul>
  </section>

  <table class="bp-range">
    <caption>Hypertensive Blood Pressure Range*</caption>
    <thead><tr><th>Age (yr)</th><th>Systolic</th><th>Diastolic</th></tr></thead>
    <tbody>
      <tr><td>newborn</td><td>&gt;97</td><td>&gt;70</td></tr>
      <tr><td>1-3</td><td>&gt;105</td><td>&gt;61</td></tr>
      <tr><td>4-12</td><td>&gt;113</td><td>&gt;86</td></tr>
    </tbody>
  </table>

  <aside class="caution">
    <svg class="caution-icon" width="54" height="48" viewBox="0 0 54 48" aria-hidden="true">
      <path d="M27 3 L51 44 Q52 46 50 46 L4 46 Q2 46 3 44 Z" fill="#fff" stroke="#fff" stroke-width="3" stroke-linejoin="round"/>
      <rect x="24" y="15" width="6" height="18" rx="3" fill="#dc4a53"/>
      <circle cx="27" cy="39" r="3.3" fill="#dc4a53"/>
    </svg>
    <p class="caution-text"><span class="caution-label">CAUTION:</span>Anti-hypertensive drugs are almost never needed for routine pediatric cases. These medications are used almost exclusively for specialized cardiac, neurosurgical, or endocrine (pheochromocytoma) cases. Consult an expert before use. Rule-out increased ICP.</p>
  </aside>

  <table class="drug-table">
    <thead><tr><th>Action</th><th>Drug (IV Dosing)</th></tr></thead>
    <tbody>
      <tr style="height:80px">
        <td class="drug-action">Direct smooth muscle relaxation</td>
        <td><ul class="drug-list">
          <li>Sodium nitroprusside 0.5-10 MICROgrams/kg/min</li>
          <li>HydrALAZINE 0.1-0.2 mg/kg (adult dose 5-10 mg)</li>
        </ul></td>
      </tr>
      <tr style="height:113px">
        <td class="drug-action">β-Adrenergic<br>blockade</td>
        <td><ul class="drug-list">
          <li>Esmolol 100-500 MICROgrams/kg over 5 min, then<br>25-300 MICROgrams/kg/min</li>
          <li class="spaced">Labetalol (also a effect) 0.2-1 mg/kg q 10 min; 0.4-3 mg/kg/hour (infusion)</li>
        </ul></td>
      </tr>
      <tr style="height:76px">
        <td class="drug-action">Calcium channel<br>blockade</td>
        <td><ul class="drug-list">
          <li>niCARdapine 0.5-5 MICROgrams/kg/min</li>
          <li class="spaced">Clevidipine 0.5-3.5 MICROgrams/kg/min</li>
        </ul></td>
      </tr>
      <tr style="height:46px">
        <td class="drug-action">D1-dopamine agonist</td>
        <td><ul class="drug-list"><li>Fenoldopam 0.2-0.8 MICROgrams/kg/min</li></ul></td>
      </tr>
    </tbody>
  </table>

  <h2 class="differential-title">CONSIDER DIFFERENTIAL (PARTIAL):</h2>
  <ul class="differential-list col-a">
    <li>Light anesthesia (consider vaporizer or infusion pump empty or malfunctioning)</li>
    <li>Hypercarbia</li>
  </ul>
  <ul class="differential-list col-b">
    <li>Hypoxemia</li>
    <li>Arterial line transducer too low or BP cuff too small</li>
    <li>Withdrawal (EtOH or opioid)</li>
  </ul>
  <ul class="differential-list col-c">
    <li>Thyroid Storm</li>
    <li>Pheochromocytoma</li>
    <li>Drug Error</li>
  </ul>

  <footer class="page-footer"></footer>
</body>
</html>
```